The Quiet Pantry Method: Reshape Your Habits Around Meals in Only 30 Days

I want a book cover for a paperback non-fiction book 30 day challenge to transform you relationship with your food, diet and lifestyle for longterm health and vitality. I would like to incorporate two photos on the front cover, one of a Greek salad and one of me the author. I have uploaded the four photos. Use which of each pair you think best. Because of my name, I want the photo on the cover. Otherwise folks assume Marla is a guy.
I am looking at best selling health books and they seem to be on the lighter side color-wise, with horizontal design. Green and orange seem to work most often, though my logo is a bluish turquoise (https://marlavoskin.com). I would imagine a light background, clear simple fonts. Looking forward to your designs!

Target Market(s)

Women around 35-40 confused by conflicting nutrition information but dedicated to better health haelthy

Industry/Entity Type

nutrition and wellness

Font styles to use
Serif

Colors
00AB8E
00BBA5
67D7C9
C6EFE9
E9F9F6
F0912C
F2A743
F7CA91
FBE8D2
FDF5EE
EE7325
F08F49
F5BC92
FAE3D3
FDF4ED

Requirements
Must have
• Clear simple look with room for an endorsement
Nice to have
• Hints of natural scenes and happy places
Should not have
• Dark or ominous feel

```html
<!DOCTYPE html>
<html lang="en">
<head>
<meta charset="utf-8">
<title>The Quiet Pantry Method – Front Cover</title>
<link rel="stylesheet" href="https://fonts.googleapis.com/css2?family=Oswald:wght@600;700&family=Dancing+Script:wght@500&family=Arimo:wght@700&display=swap">
<style>
  :root {
    --page-bg: #d9d9d9;
    --mint: #c3ece3;
    --mint-deep: #a6dfd4;
    --teal: #1a9cab;
    --ink: #111111;
    --orange: #f58a25;
    --orange-soft: #fba34e;
    --peach: #fdc48f;
    --white: #ffffff;
    --photo-hair: #b49084;
    --photo-top: #f1cfc6;
    --photo-bottom: #f9e7e2;
  }
  html, body {
    margin: 0;
    width: 1200px;
    height: 960px;
    overflow: hidden;
    background: var(--page-bg);
  }
  .cover {
    position: absolute;
    left: 290px;
    top: 50px;
    width: 620px;
    height: 860px;
    background: var(--white);
    overflow: hidden;
    box-shadow: 0 10px 30px rgba(0,0,0,0.18);
  }
  .cover-art {
    position: absolute;
    inset: 0;
  }
  .author-photo {
    position: absolute;
    left: 30px;
    top: 300px;
    width: 370px;
    height: 460px;
    background: linear-gradient(180deg, var(--photo-hair) 0%, var(--photo-top) 35%, var(--photo-bottom) 100%);
    -webkit-mask-image: radial-gradient(ellipse 50% 50% at 50% 50%, #000 70%, transparent 100%);
    mask-image: radial-gradient(ellipse 50% 50% at 50% 50%, #000 70%, transparent 100%);
  }
  .title {
    position: absolute;
    left: 0;
    right: 0;
    top: 34px;
    margin: 0;
    text-align: center;
    font-family: "Oswald", sans-serif;
    font-weight: 700;
    font-size: 50px;
    line-height: 1;
    color: var(--teal);
    letter-spacing: 0.5px;
  }
  .subtitle {
    position: absolute;
    left: 0;
    right: 0;
    top: 98px;
    margin: 0;
    text-align: center;
    font-family: "Oswald", sans-serif;
    font-weight: 600;
    font-size: 36px;
    line-height: 1;
    color: var(--ink);
  }
  .big-number {
    position: absolute;
    right: 36px;
    top: 170px;
    font-family: "Oswald", sans-serif;
    font-weight: 700;
    font-size: 200px;
    line-height: 1;
    color: var(--orange);
    letter-spacing: 6px;
  }
  .timeline {
    position: absolute;
    right: 22px;
    top: 160px;
    margin: 0;
    font-family: "Dancing Script", cursive;
    font-weight: 500;
    font-size: 44px;
    line-height: 1;
    color: var(--ink);
    white-space: nowrap;
  }
  .timeline .gap { display: inline-block; width: 70px; }
  .author-name {
    position: absolute;
    right: 80px;
    bottom: 60px;
    margin: 0;
    font-family: "Arimo", sans-serif;
    font-weight: 700;
    font-size: 32px;
    color: var(--white);
    transform: rotate(-4deg);
  }
</style>
</head>
<body>
  <main class="cover">
    <svg class="cover-art" viewBox="0 0 620 860" width="620" height="860" aria-hidden="true">
      <path d="M0 0 H620 V400 Q320 430 0 500 Z" fill="var(--mint)"/>
      <path d="M0 490 Q320 420 620 390 V402 Q320 432 0 502 Z" fill="var(--mint-deep)"/>
      <path d="M0 760 Q330 720 620 650 V860 H0 Z" fill="var(--peach)"/>
      <path d="M0 810 Q330 770 620 715 V860 H0 Z" fill="var(--orange-soft)"/>
    </svg>

    <div class="author-photo" role="img" aria-label="Photo of the author smiling in a pink blouse, holding a bowl of Greek salad"></div>

    <h1 class="title">The Quiet Pantry Method:</h1>
    <p class="subtitle">Reshape Your Habits Around Meals</p>
    <div class="big-number">30</div>
    <p class="timeline">in Only<span class="gap"></span>Days</p>

    <p class="author-name">Marla Voskin</p>
  </main>
</body>
</html>
```